Flyer for a marketing

We are a holistic mental health facility in need of a flyer to help promote our services and encourage more people to seek care. See the attachment to tell you more. We prefer warm green colors or rich blue. Thank you.

```html
<!DOCTYPE html>
<html lang="en">
<head>
<meta charset="utf-8">
<title>Evergreen Mind Health and Wellness – Flyer</title>
<link href="https://fonts.googleapis.com/css2?family=Montserrat:wght@700;800&family=Playfair+Display:wght@700;900&family=Poppins:wght@400;500;600;700&display=swap" rel="stylesheet">
<style>
  :root{
    --page-bg:#ececec;
    --paper:#ffffff;
    --green-dark:#1d5a34;
    --green:#2f8a3c;
    --green-bright:#43a047;
    --lime:#b7dc6a;
    --orange:#f4a100;
    --ink:#333a36;
    --hero-left:#6b4a38;
    --hero-right:#dfe7df;
  }
  *{box-sizing:border-box;margin:0;padding:0}
  html,body{width:1200px;height:2820px;overflow:hidden}
  body{background:var(--page-bg);font-family:"Poppins",sans-serif;color:var(--ink);position:relative}

  .flyer{position:absolute;left:50px;top:610px;width:1100px;height:1600px;background:var(--paper);overflow:hidden;box-shadow:0 6px 24px rgba(0,0,0,.18)}

  /* hero */
  .hero{position:absolute;left:0;top:0;width:1100px;height:600px}
  .hero-photo{position:absolute;inset:0;background:linear-gradient(90deg,var(--hero-left) 0%,#a07a5e 30%,#c9c2a8 48%,#c5d4c2 62%,var(--hero-right) 100%)}
  .brand{position:absolute;right:60px;top:56px;display:flex;align-items:center;gap:18px}
  .brand-mark{width:58px;height:58px;background:var(--green)}
  .brand-name{font-family:"Playfair Display",serif;font-weight:700;font-size:24px;line-height:1.15;color:var(--green-dark);width:180px}
  .tagline{position:absolute;right:70px;top:225px;font-family:"Playfair Display",serif;font-weight:900;color:var(--green-dark);text-align:right;line-height:.95}
  .tagline .small{font-size:50px}
  .tagline .big{font-size:104px}
  .tagline .line1{display:block;margin-right:200px}
  .tagline .line2{display:block;text-align:left;margin-left:60px}

  /* middle band */
  .title-panel{position:absolute;left:0;top:600px;width:445px;height:460px;background:var(--green-dark);padding:36px 30px 0 36px}
  .title-panel h1{font-family:"Montserrat",sans-serif;font-weight:800;font-size:48px;line-height:1.1;color:#fff;text-transform:uppercase}
  .title-panel h1 .accent{color:var(--orange)}
  .title-panel p{margin-top:26px;font-family:"Montserrat",sans-serif;font-weight:700;font-size:29px;line-height:1.2;color:var(--lime)}

  .photo{position:absolute;border-radius:10px}
  .photo-group{left:460px;top:608px;width:628px;height:250px;background:linear-gradient(90deg,#6f5444,#b38f74 40%,#8a6a57 70%,#c8a98f)}
  .photo-walk{left:460px;top:868px;width:210px;height:184px;background:linear-gradient(160deg,#7c8e5c,#9aa37e 50%,#5c6e43)}
  .photo-comfort{left:680px;top:868px;width:200px;height:184px;background:linear-gradient(160deg,#d9cfc4,#b89f8d 55%,#8f7a6a)}
  .photo-session{left:890px;top:868px;width:198px;height:184px;background:linear-gradient(160deg,#e6e9ec,#c4cdd6 55%,#8d9aa6)}

  /* info */
  .info{position:absolute;left:40px;top:1082px;width:1030px}
  .info .lead{font-weight:700;font-size:27px;line-height:1.4;color:var(--green-bright)}
  .info .intro{font-size:20px;line-height:1.35;margin-top:4px}
  .info h2{font-weight:700;font-size:26px;line-height:1.4;color:var(--green);margin-top:22px}
  .info ul{list-style:none;margin-top:8px;width:740px}
  .info li{font-size:20px;line-height:1.35;margin-bottom:10px}
  .info li:last-child{margin-bottom:0}
  .illustration{position:absolute;left:790px;top:1200px;width:290px;height:200px;background:radial-gradient(circle at 30% 50%,#f0c7b0 0,#e8e0d8 40%,transparent 65%),radial-gradient(circle at 75% 50%,#d7dbe0 0,#eef0f2 45%,transparent 70%),#fff}

  /* footer */
  .footer{position:absolute;left:0;bottom:0;width:1100px;height:110px;background:var(--green-dark);display:flex;align-items:center;justify-content:space-between;padding:0 36px;color:#fff;font-size:17px;line-height:1.45}
  .footer .name{color:var(--orange);font-weight:600}
  .footer .phones{color:var(--orange);font-weight:600}
  .footer .phones span{color:#fff;font-weight:400}
  .footer .web{color:#d9e8d9}
</style>
</head>
<body>
  <main class="flyer">
    <section class="hero">
      <div class="hero-photo" role="img" aria-label="Photo of a smiling young woman with curly hair outdoors, soft green background"></div>
      <div class="brand">
        <span class="brand-mark"></span>
        <span class="brand-name">Evergreen Mind Health and Wellness</span>
      </div>
      <div class="tagline">
        <span class="line1"><span class="small">The</span></span>
        <span class="big">Care</span> <span class="small">You</span>
        <span class="line2 big">Deserve</span>
      </div>
    </section>

    <section class="title-panel">
      <h1>Evergreen Mind Health and <span class="accent">Wellness</span></h1>
      <p>Where deserving patients meet compassionate providers.</p>
    </section>

    <div class="photo photo-group" role="img" aria-label="Photo of a diverse group of smiling people"></div>
    <div class="photo photo-walk" role="img" aria-label="Photo of an older couple walking outdoors"></div>
    <div class="photo photo-comfort" role="img" aria-label="Photo of a person comforting a friend"></div>
    <div class="photo photo-session" role="img" aria-label="Photo of a counseling session"></div>

    <section class="info">
      <div class="lead">We are accepting new patients, no waiting list.</div>
      <p class="intro">Your mental health matters, so make it a priority and call us today for an appointment.</p>
      <h2>Why choose us?</h2>
      <ul>
        <li>We are an integrative holistic psychiatric center.</li>
        <li>Our mission is to provide compassionate quality care.</li>
        <li>We provide psychiatric services including medication management and psychotherapy.</li>
        <li>We listen, care, and empower you to live better.</li>
        <li>We accept major insurances.</li>
      </ul>
    </section>
    <div class="illustration" role="img" aria-label="Illustration of two head profiles with colorful puzzle brain pieces"></div>

    <footer class="footer">
      <div class="address"><div class="name">Evergreen Mind Health and Wellness</div>4810 Willowbrook Lane, Suite 120 Fairview, CA 90000</div>
      <div class="phones">Ph: <span>(555) 010-4420</span><br>Fax: <span>(555) 010-8813</span></div>
      <div class="web">info@evergreenmindhealth.com<br>evergreenmindhealth.com</div>
    </footer>
  </main>
</body>
</html>
```